依頼詳細
シュリンクラベルを新しいデザインに変更する目的は、ヘアトリートメントも同じ容器でシリーズとしてのリニューアル新発売します(今までは100mlと少量)ので、2アイテムの関連性とシンプルでいて、新しいデザインで、2本揃えて購入したくなるようなデザイン、バスルームに置いていても、心地よいデザインにしたいからです。容器の素材はPP、 ラベルはシュリンクのPET素材ですから、写真は半透明になりますし、写真ではリアルさを伝えられないので、現在のデザインのように全面に使用しなくても良いと思います、美しい淡い色のグラデか、写真を入れた方が良いのか、他の商品のラベルデザインも参考にしていただきたいです。ロゴは金ホットスタンプを使用してください。
シャンプー1000mlのお徳用サイズは、金ホットスタンプは使用無しでデザインしてください。
記載項目
ラベル:デジタル印刷シュリンク(箔押しアリ) 印刷範囲用データ添付しますから、ここにレイアウトデザインしてください 現在のシャンプー・トリートメント画像も添付します ロゴも添付します 金ホットスタンプ・箔のサイズ: タテ45㎜×ヨコ50㎜ 以内にお願いします
お徳用サイズは、現在のデータを添付します。

希望イメージ
シンプル 複雑
単色 カラフル
暗い 明るい
日常 高級
遊び心 厳粛
未来的 伝統的
女性的 男性的
希望する色
水色系、紫系、金色
納品ファイル
• イラストレーター形式 (.ai)
補足説明
ロゴは、添付のクレイクレンジング・クレイクレンジング・フェイス&ボディソープのロゴに準じてください。今現在のロゴの特に、ラグジュアリーの英字ロゴは、変えてください。トリートメントは、英字のトリートメントは変えないで、現在のを使用しても可能です。
シャンパーニュとヘアトリートメントのそれぞれのテキストデータをイラストレーターで作成しました、添付します。
こちらのテキストを使用してください。
ロゴは、参考にするだけで、TOMIRENOは、クレイクレンジングやクリアクレンジングウォーターと同じにしてください。SHAMPOOやHAIR TREATMENTは新たにデザインご提案してください。
前記の追記の冒頭に「シャンパーニュ」と記載しましたが、「シャンプー」の誤入力です、訂正させていただきます

TMIRENOロゴ・ヘアトリートメントのJANコードを上書きした「text.ai」を添付しますので、こちらで制作をお願いします
参考のために、当社の ①フェイス&ボディソープ  ②クリアクレンジングウォーター  ③クレイクレンジング、 3アイテムの新ラベルデザインを添付ファイル 「ラベルデザイン新シリーズJpg」をご覧いただきますよう、お願いいたします。
このバラの写真のコラージュの色相・明度バリエーションで構成した3点のラベルのイメージに併せるなら、シャンプーのラベルは、香りに使用しているラベンダーやゼラニウムの写真のコラージュのバリエーションが良いのかなと思います。
しかし、個性的過ぎるし、シャンプーは男性も愛用者が多いですので、シンプルにした方が良いのか、どの方向がお客様に喜ばれるか、当社のイメージも考慮しながら、
ご提案くださいますと、ありがたく思います。どうぞ、よろしくお願いいたします。
添付の資料に不備があり、申し訳ありません、締め切りを2日延長いたします。
補足説明です、よろしくお願いいたします。

1.現在のシャンプー商品画像jpgを添付します(容器のポンプの色は白色です)
この容器を シャンプーとトリートメント両方に使用します

2.textのpdfファイルを添付します、.aiファイルが文字化けする場合は、このpdfファイルを見てください

3.シャンプーの香り成分は、天然のラベンダーがメインでゼラニウム(とオレンジ)の香り成分も配合しています

4.トリートメントもシャンプーと同じ香りの予定ですが、ホホバ種子オイルを配合していることも、大きなポイントです
■ 選んだ理由

こちらのデザインは、ベースのグラデーションの色彩、英字フォント、ラベンダーとゼラニウムの画像のコラージュ、全てがブランドイメージを高める素晴らしいデザインだと思います。修正依頼にも快く応じて頂き、ありがとうございました。

■ 提案者全員のお礼・コメント

私の認識不足で、選択のタイミングが遅くなり、申し訳ございませんでした。
ご提案は、いろいろなタイプのデザインがありました。ブランドイメージの幅が広がりました。貴重なご提案を本当にありがとうございました。

```html
<!DOCTYPE html>
<html lang="ja">
<head>
<meta charset="utf-8">
<title>TMIRENO Shampoo &amp; Hair Treatment Labels</title>
<link href="https://fonts.googleapis.com/css2?family=Cinzel:wght@500&family=Noto+Serif+JP:wght@400;500&family=Great+Vibes&family=Playball&display=swap" rel="stylesheet">
<style>
  :root {
    --page: #f4f1f4;
    --label-top: #ffffff;
    --label-mid: #f3eef6;
    --label-low: #e4d3ec;
    --label-base: #e9b9c6;
    --ink: #4a3f4c;
    --gold: #b8954a;
    --lavender: #9a7cc0;
    --lavender-deep: #7c5ca8;
    --wreath-soft: #e7dcef;
    --wreath-leaf: #b9c9a7;
  }
  * { margin: 0; padding: 0; box-sizing: border-box; }
  html, body { width: 798px; height: 1200px; overflow: hidden; background: var(--page); }
  .canvas {
    width: 798px; height: 1200px;
    display: flex; justify-content: center; align-items: center; gap: 26px;
  }
  .label {
    position: relative;
    width: 370px; height: 1110px;
    background: linear-gradient(180deg, var(--label-top) 0%, var(--label-mid) 45%, var(--label-low) 72%, var(--label-base) 100%);
    border-radius: 6px;
    box-shadow: 0 0 0 1px rgba(0,0,0,0.04);
    text-align: center;
    color: var(--ink);
    font-family: "Noto Serif JP", serif;
  }
  .tagline { position: absolute; top: 48px; width: 100%; font-size: 21px; letter-spacing: 2px; }
  .brand {
    position: absolute; top: 92px; width: 100%;
    font-family: "Cinzel", serif; font-weight: 500;
    font-size: 58px; letter-spacing: 5px; color: var(--gold);
  }
  .wreath {
    position: absolute; left: 40px; top: 200px; width: 290px; height: 300px;
  }
  .product-name {
    position: absolute; top: 300px; width: 100%;
    font-family: "Playball", cursive; color: var(--lavender-deep);
    font-size: 46px; line-height: 1;
  }
  .product-name.two-line { top: 268px; line-height: 1.05; }
  .line-name {
    position: absolute; top: 380px; width: 100%;
    font-family: "Great Vibes", cursive; color: var(--lavender);
    font-size: 72px; line-height: 1;
  }
  .flower-cluster {
    position: absolute; left: 125px; top: 478px; width: 120px; height: 60px;
  }
  .jp-name { position: absolute; top: 580px; width: 100%; font-size: 24px; line-height: 1.7; letter-spacing: 2px; }
  .volume {
    position: absolute; top: 770px; left: 50%; transform: translateX(-50%);
    width: 62px; height: 36px; border: 1.5px solid var(--ink);
    font-size: 15px; line-height: 33px;
  }
  .origin { position: absolute; top: 855px; width: 100%; font-size: 19px; letter-spacing: 2px; }
</style>
</head>
<body>
<main class="canvas">

  <section class="label label--shampoo">
    <p class="tagline">自然からの贈りもの</p>
    <h1 class="brand">TMIRENO</h1>
    <svg class="wreath" viewBox="0 0 290 300" role="img" aria-label="Lavender sprigs and a leafy wreath framing the product name">
      <defs>
        <radialGradient id="wreathShampoo" cx="50%" cy="50%" r="50%">
          <stop offset="70%" stop-color="#ffffff" stop-opacity="0"/>
          <stop offset="88%" stop-color="#e7dcef"/>
          <stop offset="100%" stop-color="#ffffff" stop-opacity="0"/>
        </radialGradient>
      </defs>
      <ellipse cx="145" cy="150" rx="140" ry="145" fill="url(#wreathShampoo)"/>
    </svg>
    <p class="product-name">Shampoo</p>
    <p class="line-name">Luxury</p>
    <svg class="flower-cluster" viewBox="0 0 120 60" role="img" aria-label="Small cluster of lavender-coloured flowers">
      <ellipse cx="60" cy="30" rx="58" ry="26" fill="#c4aee0" opacity="0.75"/>
    </svg>
    <p class="jp-name">トミレノ<br>シャンプー<br>ラグジュアリー</p>
    <div class="volume">300ml</div>
    <p class="origin">MADE IN JAPAN</p>
  </section>

  <section class="label label--treatment">
    <p class="tagline">自然からの贈りもの</p>
    <h1 class="brand">TMIRENO</h1>
    <svg class="wreath" viewBox="0 0 290 300" role="img" aria-label="Lavender sprigs and a leafy wreath framing the product name">
      <defs>
        <radialGradient id="wreathTreatment" cx="50%" cy="50%" r="50%">
          <stop offset="70%" stop-color="#ffffff" stop-opacity="0"/>
          <stop offset="88%" stop-color="#e7dcef"/>
          <stop offset="100%" stop-color="#ffffff" stop-opacity="0"/>
        </radialGradient>
      </defs>
      <ellipse cx="145" cy="150" rx="140" ry="145" fill="url(#wreathTreatment)"/>
    </svg>
    <p class="product-name two-line">Hair<br>Treatment</p>
    <p class="line-name">Luxury</p>
    <svg class="flower-cluster" viewBox="0 0 120 60" role="img" aria-label="Small cluster of lavender-coloured flowers">
      <ellipse cx="60" cy="30" rx="58" ry="26" fill="#c4aee0" opacity="0.75"/>
    </svg>
    <p class="jp-name">トミレノ<br>ヘアトリートメント<br>ラグジュアリー</p>
    <div class="volume">300ml</div>
    <p class="origin">MADE IN JAPAN</p>
  </section>

</main>
</body>
</html>
```